I am a Vantrell Service and Marketing Consultant looking for a Vantrellesque but business like cover wit

I need a bookcover designed for my new business book titled; "Orderly Wonder. 7 Bright Doors To Vantrellize Your Firm. Outshine, Outlast & Outgrow Your Rivals in EVERY Climate"

The name of my company is Harbor Care Today

We work with companies to implement Vantrell Style Service and Themeing, and then create marketing campaigns to promote that level of service.

I have used Owl Whisper font in the past, but am not tied to it

Target Market(s)

Small Business owners, medical practices, law firms

Industry/Entity Type

Business

Requirements
Must have
• Colors: RGB 30, 54, 128 AND 113, 191, 76. These are the two colors in my logo, if you need it.
Nice to have
• Magic Key?? Gloved Hand (similar to a Vantrell Character)??
Should not have
• Any copyright protected inages

```html
<!DOCTYPE html>
<html lang="en">
<head>
<meta charset="UTF-8">
<title>Orderly Wonder – Book Cover</title>
<link rel="stylesheet" href="https://fonts.googleapis.com/css2?family=Teko:wght@300;400;600&family=Oswald:wght@600&family=Roboto+Condensed:wght@300;700&family=Open+Sans:wght@700&display=swap">
<style>
  :root {
    --stage: #e6e6e6;
    --cover: #e9e9e9;
    --spine: #dcdcdc;
    --ink: #1b1b1b;
    --hat-dark: #1d1f24;
    --hat-mid: #3a3d44;
    --brand-blue: rgb(30, 54, 128);
    --brand-green: rgb(113, 191, 76);
    --isbn-box: #0d0d0d;
    --isbn-text: #ffffff;
  }
  * { box-sizing: border-box; margin: 0; padding: 0; }
  html, body { width: 1200px; height: 800px; overflow: hidden; }
  body { background: var(--stage); color: var(--ink); }

  .cover-spread {
    position: absolute;
    left: 176px; top: 100px;
    display: flex;
    height: 600px;
    box-shadow: 0 10px 30px rgba(0,0,0,0.12);
  }

  /* Back cover */
  .back-cover {
    width: 400px; height: 100%;
    background: var(--cover);
    padding: 26px 30px 24px;
    position: relative;
  }
  .back-cover__author {
    text-align: right;
    font-family: "Roboto Condensed", sans-serif;
    font-weight: 700;
    font-size: 14px;
  }
  .back-cover__title {
    font-family: "Teko", sans-serif;
    font-weight: 600;
    font-size: 44px;
    line-height: 0.95;
    letter-spacing: 1px;
    text-transform: uppercase;
    white-space: nowrap;
    margin-top: 4px;
  }
  .back-cover__subtitle {
    font-family: "Oswald", sans-serif;
    font-weight: 600;
    font-size: 15.5px;
    text-transform: uppercase;
    white-space: nowrap;
    margin-top: 0;
  }
  .back-cover__blurb {
    font-family: "Open Sans", sans-serif;
    font-weight: 700;
    font-size: 8.6px;
    line-height: 13.3px;
    text-align: justify;
    margin-top: 10px;
  }
  .back-cover__publisher {
    position: absolute;
    left: 30px; bottom: 40px;
    display: flex; align-items: center; gap: 6px;
    font-family: "Roboto Condensed", sans-serif;
    font-weight: 700;
    font-size: 12px;
    color: var(--brand-blue);
  }
  .back-cover__publisher-dot {
    width: 16px; height: 16px; border-radius: 50%;
    background: var(--brand-green);
  }
  .back-cover__isbn {
    position: absolute;
    right: 30px; bottom: 24px;
    width: 108px; height: 70px;
    background: var(--isbn-box);
    color: var(--isbn-text);
    font-family: "Roboto Condensed", sans-serif;
    font-weight: 300;
    font-size: 15px;
    display: flex; align-items: center; justify-content: center;
  }

  /* Spine */
  .spine {
    width: 48px; height: 100%;
    background: var(--spine);
    position: relative;
  }
  .spine__text {
    position: absolute;
    left: 50%; top: 20px;
    transform-origin: 0 0;
    transform: rotate(90deg) translateY(-50%);
    white-space: nowrap;
    display: flex; align-items: baseline; gap: 34px;
  }
  .spine__title {
    font-family: "Teko", sans-serif;
    font-weight: 600;
    font-size: 36px;
    letter-spacing: 7px;
    text-transform: uppercase;
    line-height: 1;
  }
  .spine__author {
    font-family: "Roboto Condensed", sans-serif;
    font-weight: 700;
    font-size: 12px;
  }

  /* Front cover */
  .front-cover {
    width: 400px; height: 100%;
    background: var(--cover);
    text-align: center;
    padding-top: 36px;
  }
  .front-cover__title-top {
    display: block;
    font-family: "Teko", sans-serif;
    font-weight: 400;
    font-size: 52px;
    letter-spacing: 7px;
    line-height: 1;
    text-transform: uppercase;
  }
  .front-cover__title-main {
    display: block;
    font-family: "Teko", sans-serif;
    font-weight: 600;
    font-size: 110px;
    line-height: 0.85;
    text-transform: uppercase;
    white-space: nowrap;
    margin-top: 10px;
  }
  .front-cover__art {
    display: block;
    margin: 24px auto 0;
  }
  .front-cover__subtitle {
    font-family: "Oswald", sans-serif;
    font-weight: 600;
    font-size: 16.5px;
    text-transform: uppercase;
    white-space: nowrap;
    margin-top: 20px;
  }
  .front-cover__tagline {
    font-family: "Roboto Condensed", sans-serif;
    font-weight: 300;
    font-size: 22px;
    line-height: 1.1;
    margin-top: 10px;
  }
  .front-cover__tagline strong { font-weight: 700; }
  .front-cover__author {
    font-family: "Roboto Condensed", sans-serif;
    font-weight: 700;
    font-size: 14px;
    margin-top: 12px;
  }
</style>
</head>
<body>
  <main class="cover-spread">
    <section class="back-cover">
      <p class="back-cover__author">Author Name</p>
      <h2 class="back-cover__title">Orderly Wonder</h2>
      <p class="back-cover__subtitle">7 Bright Doors To Vantrellize Your Firm</p>
      <p class="back-cover__blurb">
        Lorem ipsum dolor sit amet, consectetur adipisicing elit, sed do eiusmod tempor incididunt ut labore et dolore magna aliqua. Ut enim ad minim veniam, quis nostrud exercitation.
        Lorem ipsum dolor sit amet, consectetur adipisicing elit, sed do eiusmod tempor incididunt ut labore et dolore magna aliqua. Ut enim ad minim veniam, quis nostrud exercitation.
        Lorem ipsum dolor sit amet, consectetur adipisicing elit, sed do eiusmod tempor incididunt ut labore et dolore magna aliqua. Ut enim ad minim veniam, quis nostrud exercitation.
        Lorem ipsum dolor sit amet, consectetur adipisicing elit, sed do eiusmod tempor incididunt ut labore et dolore magna aliqua. Ut enim ad minim veniam, quis nostrud exercitation.
        Lorem ipsum dolor sit amet, consectetur adipisicing elit, sed do eiusmod tempor incididunt ut labore et dolore magna aliqua. Ut enim ad minim veniam, quis nostrud exercitation.
        Lorem ipsum dolor sit amet, consectetur adipisicing elit, sed do eiusmod tempor incididunt ut labore et dolore magna aliqua. Ut enim ad minim veniam, quis nostrud exercitation.
        Lorem ipsum dolor sit amet, consectetur adipisicing elit, sed do eiusmod tempor incididunt ut labore et dolore magna aliqua. Ut enim ad minim veniam, quis nostrud exercitation.
        Lorem ipsum dolor sit amet, consectetur adipisicing elit, sed do eiusmod tempor incididunt ut labore et dolore magna aliqua. Ut enim ad minim veniam, quis nostrud exercitation.
      </p>
      <div class="back-cover__publisher">
        <span class="back-cover__publisher-dot"></span>
        <span>Harbor Care Today</span>
      </div>
      <div class="back-cover__isbn">ISBN</div>
    </section>

    <section class="spine">
      <div class="spine__text">
        <span class="spine__title">Orderly Wonder</span>
        <span class="spine__author">Author Name</span>
      </div>
    </section>

    <section class="front-cover">
      <h1>
        <span class="front-cover__title-top">Orderly</span>
        <span class="front-cover__title-main">Wonder</span>
      </h1>
      <svg class="front-cover__art" width="290" height="176" viewBox="0 0 290 176" role="img" aria-label="Photograph of a black magician's top hat shown upside down">
        <defs>
          <linearGradient id="hatShade" x1="0" y1="0" x2="1" y2="0">
            <stop offset="0" stop-color="var(--hat-dark)"/>
            <stop offset="0.5" stop-color="var(--hat-mid)"/>
            <stop offset="1" stop-color="var(--hat-dark)"/>
          </linearGradient>
        </defs>
        <rect x="0" y="0" width="290" height="176" rx="14" fill="url(#hatShade)"/>
      </svg>
      <p class="front-cover__subtitle">7 Bright Doors To Vantrellize Your Firm</p>
      <p class="front-cover__tagline">
        <strong>Outshine</strong>, <strong>Outlast</strong> &amp; <strong>Outgrow</strong><br>
        Your <strong>Rivals</strong> in <strong>EVERY</strong> Climate
      </p>
      <p class="front-cover__author">Author Name</p>
    </section>
  </main>
</body>
</html>
```